Seminar Invitation for Financial Planning Group

I want a flyer that I can mail out to 5000 people (targeted group of seniors with high incomes and that own homes) to invite to a seminar we will be holding on March 9th and March 10th of 2010. It is a FREE educational workshop and we want to have a colorful catchy flyer that we will be mailing out that doesn't look to cheesy or like a get rich quick scheme. We are experienced financial planners that are proposing long term practical solutions.

Dates and Locations:
March 9th, 2010- Halvern Quastel 5:30 p.m.-7:00 p.m.
March 11th, 2010-Vista Calloway Vineyard 11:00 a.m. -12:30 p.m.

Speakers:
Desmond T. Marquill, ChFC and CLU, focuses on the coordination of insurance, retirement, and estate planning. Des is a member of the Guild of Wealth Advisory Practitioners.
Paul Demontavo, C.F.A., is V.P. of Investment Research at Keystrand Advisory and is a member of the Tremonton Circle of Portfolio Examiners.

Another Speaker:

Social Security Public Relations Director, TBA

At the bottom, it should read, and in similar font as I am posting now:

Desmond T. Marquill is a registered representatie with & securities are offered through Keystrand Advisory, Inc. Member VELTRA/GOBAX CA Insurance License # 0817265 (03-2010)

The font size should be around 12 point

Also, we now have the same of the Social Security Speaker( to go Under Desmond T. Marquill and Paul Demontavo),

Marisol Pennick, San Diego Social Security Public Affairs Specialist

Also, please incorporate at the bottom(the first line and phone number/email should be large compared to the rest of the text so it is easy to locate contact info:

To register, please call (555) 271-9036 or email hilda@marquillbrest.example.

Due to limited capacity, we reserve the right to refuse unregistered guests. Complimentary parking is provided.

CORRECT DATES AND LOCATIONS ARE:
3/9/10 5:30-7:00PM HALVERN QUASTEL
3/10/10 11:00-12:30 P.M. VISTA CALLOWAY LODGE

ALSO ADD, RIGHT ABOVE THE LONG TERM CARE LINE IN THE TOPICS TO BE DISCUSSED SECTION, PLEASE ADD "Top 10 Myths About Social Security" No need for quotation marks I just want to distinguish the text here. Also, I have uploaded 2 pics, one of Paul Demontavo and one of Marisol Pennick. I am still waiting on one from Des Marquill and will post it when I receive it. These are to go to left of their name and short description. 

Target Market(s)

Seniors, People who are about to retire, 55+ in age, primarily those with investable assets of 500k+, those who are concerned with their retirement income and their nest egg.

Industry/Entity Type

Insurance

Requirements
Must have
• An Image(not to make up more than 20% of the flyer). Preferably of a family (elderly couple playing with grandkids, maybe in mid-60''s). Maybe a cartoon of a couple wondering about their financial future since the market tanked and depleted their nest egg.
• -Seminar Dates and Times
• -Must be 1 Page
• -Title of Seminar is "Back to Basics"
• 3 Speakers, each an expert in their field.
• 1)Social Security Speaker 2)Paul Demontavo, CFA, and 3) retirement planning expert, Desmond T. Marquill

• Topics to Be Discussed at Seminar:
• Roth Conversion Pitfalls and Opportunities
• Market Outlook 2010/2011
• How to Maximize Your Retirement Income
• Can You Afford to Not Have Long Term Care?
• And many more....
• Should not have
• No bags of money or bullions. We are not out to have people make a lot of money off of us, we are just advertising good solid financial advice

```html
<!DOCTYPE html>
<html lang="en">
<head>
<meta charset="utf-8">
<title>Back to Basics – Free Educational Workshop</title>
<link rel="stylesheet" href="https://fonts.googleapis.com/css2?family=Cormorant+Garamond:ital,wght@1,600&family=Didact+Gothic&family=PT+Sans:wght@400;700&family=Pinyon+Script&display=swap">
<style>
  :root {
    --green-deep: #0b7a2c;
    --green-mid: #2ea53b;
    --green-light: #86cf3c;
    --teal: #3fa9b8;
    --teal-pale: #bfe2ec;
    --ink-green: #0f5a36;
    --ink-dark: #173d22;
    --white: #ffffff;
    --panel: rgba(255, 255, 255, 0.22);
    --panel-dark: rgba(20, 90, 40, 0.25);
  }
  html, body { margin: 0; padding: 0; overflow: hidden; background: var(--white); }
  .flyer {
    position: relative;
    width: 929px;
    height: 1200px;
    overflow: hidden;
    background: var(--white);
    font-family: "PT Sans", sans-serif;
  }
  .backdrop { position: absolute; inset: 0; }
  .quote-mark {
    position: absolute;
    font-family: "Cormorant Garamond", serif;
    font-weight: 600;
    color: var(--teal-pale);
    font-size: 300px;
    line-height: 1;
  }
  .quote-open { left: 392px; top: -40px; }
  .quote-close { left: 800px; top: 60px; }
  .title-back {
    position: absolute;
    left: 404px; top: 26px;
    margin: 0;
    font-family: "Didact Gothic", sans-serif;
    font-weight: 400;
    font-size: 104px;
    line-height: 1;
    color: var(--ink-green);
    letter-spacing: -1px;
  }
  .title-basics {
    position: absolute;
    left: 448px; top: 118px;
    margin: 0;
    font-family: "Cormorant Garamond", serif;
    font-style: italic;
    font-weight: 600;
    font-size: 104px;
    line-height: 1;
    color: var(--ink-green);
  }
  .subtitle {
    position: absolute;
    left: 560px; top: 218px;
    margin: 0;
    font-size: 25px;
    color: var(--ink-green);
  }
  .script-head {
    position: absolute;
    margin: 0;
    font-family: "Pinyon Script", cursive;
    font-weight: 400;
    font-size: 36px;
    color: var(--white);
    line-height: 1;
  }
  .head-discuss { left: 16px; top: 302px; }
  .head-topics { right: 634px; top: 456px; }
  .head-speakers { left: 394px; top: 370px; }
  .head-dates { left: 526px; top: 752px; }
  .panel {
    position: absolute;
    background: var(--panel);
    border-radius: 0 12px 12px 0;
  }
  .panel-discuss { left: 0; top: 343px; width: 301px; height: 88px; }
  .panel-topics { left: 0; top: 490px; width: 301px; height: 291px; }
  .panel-speakers { left: 386px; top: 403px; width: 511px; height: 338px; border-radius: 12px; }
  .topic-list {
    list-style: none;
    margin: 0;
    padding: 0 18px 0 0;
    text-align: right;
    font-size: 20px;
    line-height: 32px;
    color: var(--ink-dark);
  }
  .panel-discuss .topic-list { padding-top: 12px; }
  .panel-topics .topic-list { padding-top: 24px; }
  .topic-list li + li { margin-top: 30px; }
  .topic-list li.tight { margin-top: 0; }
  .speaker-list {
    margin: 0;
    padding: 20px 16px 0 14px;
    color: var(--white);
    font-size: 20px;
    line-height: 30px;
  }
  .speaker-list p { margin: 0 0 30px; }
  .dates {
    position: absolute;
    left: 526px; top: 794px;
    margin: 0;
    color: var(--white);
    font-size: 20px;
    line-height: 30px;
  }
  .dates p { margin: 0 0 27px; }
  .family-photo {
    position: absolute;
    left: 0; top: 960px;
    width: 470px; height: 170px;
  }
  .firm {
    position: absolute;
    left: 600px; top: 1100px;
    width: 300px;
    color: var(--ink-green);
  }
  .firm-name { margin: 0; font-size: 17px; font-weight: 700; }
  .firm-blurb { margin: 2px 0 0; font-size: 11.5px; line-height: 13px; }
</style>
</head>
<body>
<main class="flyer">
  <svg class="backdrop" width="929" height="1200" viewBox="0 0 929 1200" aria-hidden="true">
    <defs>
      <linearGradient id="field" x1="0" y1="0" x2="1" y2="1">
        <stop offset="0" stop-color="#0b7a2c"/>
        <stop offset="0.45" stop-color="#2ea53b"/>
        <stop offset="0.75" stop-color="#1d8f33"/>
        <stop offset="1" stop-color="#0b7a2c"/>
      </linearGradient>
      <linearGradient id="glow" x1="0" y1="0" x2="1" y2="0">
        <stop offset="0" stop-color="#86cf3c" stop-opacity="0"/>
        <stop offset="0.5" stop-color="#9ad94a" stop-opacity="0.7"/>
        <stop offset="1" stop-color="#86cf3c" stop-opacity="0"/>
      </linearGradient>
    </defs>
    <path d="M0,95 C220,40 420,150 929,200 L929,240 C480,190 240,90 0,135 Z" fill="#8fd0dc" opacity="0.55"/>
    <path d="M0,150 C230,100 480,220 929,265 L929,1100 C620,1085 320,880 0,960 Z" fill="url(#field)"/>
    <path d="M0,230 C250,150 520,300 929,330 L929,420 C520,380 260,250 0,320 Z" fill="url(#glow)"/>
    <path d="M0,600 C300,520 620,760 929,700 L929,780 C600,830 320,600 0,690 Z" fill="#9ad94a" opacity="0.25"/>
    <path d="M0,940 C320,860 600,1070 929,1080" fill="none" stroke="#3fa9b8" stroke-width="14" opacity="0.8"/>
    <path d="M0,925 C320,845 600,1055 929,1065" fill="none" stroke="#bfe2ec" stroke-width="5"/>
    <path d="M0,960 C320,880 600,1090 929,1100 L929,1200 L0,1200 Z" fill="#ffffff"/>
  </svg>

  <div class="quote-mark quote-open" aria-hidden="true">&ldquo;</div>
  <div class="quote-mark quote-close" aria-hidden="true">&rdquo;</div>
  <h1 class="title-back">back</h1>
  <h1 class="title-basics">to basics</h1>
  <p class="subtitle">Free Educational Workshop</p>

  <h2 class="script-head head-discuss">Seminar will discuss:</h2>
  <section class="panel panel-discuss">
    <ul class="topic-list">
      <li>Roth Conversion Pitfalls<br>and Opportunities</li>
    </ul>
  </section>

  <h2 class="script-head head-topics">Topics:</h2>
  <section class="panel panel-topics">
    <ul class="topic-list">
      <li>Market Outlook 2010/2011</li>
      <li class="tight">How to Maximize Your<br>Retirement Income</li>
      <li>Can You Afford to Not<br>Have Long Term Care?</li>
      <li>And many more....</li>
    </ul>
  </section>

  <h2 class="script-head head-speakers">Speakers:</h2>
  <section class="panel panel-speakers">
    <div class="speaker-list">
      <p>Desmond T. Marquill, ChFC and CLU, focuses on the coordination of insurance, retirement, and estate planning. Des is a member of the Guild of Wealth Advisory Practitioners.</p>
      <p>Paul Demontavo, C.F.A., is V.P. of Investment Research at Keystrand Advisory and is a member of the Tremonton Circle of Portfolio Examiners.</p>
      <p>Social Security Public Relations Director, TBA</p>
    </div>
  </section>

  <h2 class="script-head head-dates">Dates and Locations:</h2>
  <div class="dates">
    <p>March 9th, 2010 - Halvern Quastel<br>5:30 p.m.-7:00 p.m.</p>
    <p>March 11th, 2010 - Vista Calloway Vineyard<br>11:00 a.m. -12:30 p.m.</p>
  </div>

  <svg class="family-photo" viewBox="0 0 470 170" role="img" aria-label="Photo of grandparents with two grandchildren sitting together on the grass beside a picnic basket">
    <defs>
      <radialGradient id="photoTone" cx="0.45" cy="0.55" r="0.7">
        <stop offset="0" stop-color="#e9c9a8"/>
        <stop offset="0.5" stop-color="#c9d6a4"/>
        <stop offset="1" stop-color="#ffffff" stop-opacity="0"/>
      </radialGradient>
    </defs>
    <rect width="470" height="170" fill="url(#photoTone)"/>
  </svg>

  <footer class="firm">
    <p class="firm-name">Marquill/Brest</p>
    <p class="firm-blurb">Since 1967, Marquill/Brest has provided reliable and ethical services that result in cost-effective, timely and profitable solutions for our clients.</p>
  </footer>
</main>
</body>
</html>
```